Production/Entertainment Company needs a Wonderful Wordpress Website

Bramblewick Entertainment is a production company and entertainment provider servicing Vancouver, Calgary and Toronto. The company offers a host of services that need to be streamlined into a sleeker and more fanciful website design. The priority is that potential clients who need event entertainment can easily see what Bramblewick has to offer through a sleek artistic site. Creatively innovative designs are welcomed!

See existing offering here: http://bramblewickentertainment.example/
It isn't working because so much information is being presented at once. We want to simplify, animate, and enliven the site.

See attached file for a breakdown of our initial ideas (but we're open to your creativity!), how we would like to categorize the services offered by the company into 4 sub-pages, and the header/footer descriptions we must have incorporated for our SEO

What we want to communicate is a sense of playfulness, magic, and enchantment but have it also be sleek and professional. Something easy for us to edit and update.

Target Market(s)

Clients who are looking for unique entertainment options for their private or corporate events.

Industry/Entity Type

Entertainment

Requirements
Must have
• Bramblewick is going to shift its name through this website launch from Bramblewick Entertainment to Bramblewick Productions so your attention to the logo would be great. We love the lizard images on the site and it would be great if it could be graphically integrated into the name itself.
• Same overall color scheme please - dark background with chameleon green highlights. Red and purple too.
• We would love to have a way to communicate all the entertainment options in a dynamic way on the homepage, so that so much text doesn't need to fill the site at once. For example: when the mouse hovers over a category like "Bramblewick's Characters", a list could appear with the entertainment options:
• "Star-studded impersonators
• Roving Characters
• Improv Artists
• Comedians
• Singing Telegrams
• Professional Actors & Models
• Emcees"
• (see file for other categories and options)
• We are so open to any other creative ideas you have to accomplish this streamlining in the site's design.
• Lots of potential space to upload videos and images of the amazing entertainment Bramblewick offers. A banner that shifts images would be great!

```html
<!DOCTYPE html>
<html lang="en">
<head>
<meta charset="utf-8">
<title>Bramblewick Entertainment</title>
<link rel="stylesheet" href="https://fonts.googleapis.com/css2?family=Oswald:wght@400;500&family=Arimo:wght@400;700&family=Freckle+Face&display=swap">
<style>
:root{
  --green:#3fe43a;
  --magenta:#c3137f;
  --black:#000;
  --panel:#1b1b1b;
  --panel-2:#262626;
  --rule:#3a3a3a;
  --text:#e6e6e6;
  --muted:#b5b5b5;
  --white:#fff;
}
*{margin:0;padding:0;box-sizing:border-box}
html,body{width:1200px;height:2796px;overflow:hidden}
body{background:linear-gradient(90deg,#2a2a2a 0,#0c0c0c 8%,#050505 12%,#050505 88%,#0c0c0c 92%,#2a2a2a 100%);font-family:'Arimo',sans-serif;color:var(--text);position:relative}
.abs{position:absolute}
.page{position:absolute;left:140px;top:0;width:920px;height:2652px;background:var(--black)}
.heading{font-family:'Oswald',sans-serif;font-weight:400;font-size:20px;color:var(--white);position:absolute;padding-bottom:10px;border-bottom:1px solid var(--rule)}
.logo{left:162px;top:22px;font-family:'Oswald',sans-serif;font-weight:500;font-size:42px;line-height:1;color:var(--green);letter-spacing:.5px}
.logo-sub{left:200px;top:72px;font-family:'Oswald',sans-serif;font-size:13px;color:var(--green)}
.tagline{left:200px;top:92px;font-family:'Oswald',sans-serif;font-size:14px;color:var(--muted);letter-spacing:.3px}
.social{top:14px;width:32px;height:32px;border-radius:50%;background:#3d3d3d}
.contact{right:162px;top:72px;text-align:right;font-family:'Oswald',sans-serif;color:var(--green)}
.contact .phone{font-size:22px;font-weight:500}
.contact .email{font-size:13px}
.nav{left:140px;top:140px;width:920px;height:58px;border-top:1px solid var(--rule);border-bottom:1px solid var(--rule);display:flex;align-items:center;gap:34px;padding-left:27px;font-family:'Oswald',sans-serif;font-size:15px;color:var(--white)}
.hero{left:158px;top:226px;width:884px;height:364px;background:radial-gradient(ellipse at 35% 20%,#8fb8ff 0,#3c4fa8 25%,#3a1f6b 50%,#0d0b1e 80%)}
.hero-caption{left:158px;top:366px;width:452px;height:94px;background:rgba(30,30,30,.85);font-family:'Oswald',sans-serif;font-size:26px;line-height:34px;color:var(--white);padding:13px 20px}
.dots{left:566px;top:608px;display:flex;gap:6px}
.dots i{width:11px;height:11px;border-radius:50%;background:#555;display:block}
.dots i:first-child{background:#aaa}
.svc{width:434px;height:237px;display:flex}
.svc .txt{width:255px;background:var(--magenta);padding:12px 14px}
.svc .pic{flex:1;background:linear-gradient(135deg,#555,#161616)}
.svc h3{font-family:'Oswald',sans-serif;font-weight:400;font-size:19px;line-height:23px;color:var(--white);text-transform:uppercase;margin-bottom:6px}
.svc ul{list-style:none;padding-left:12px;font-family:'Oswald',sans-serif;font-size:15px;line-height:22.5px;color:var(--white)}
.video{left:158px;top:1284px;width:532px;height:296px;border:3px solid #3a3a3a;background:linear-gradient(160deg,#d9d2c4,#8c8276 55%,#5a524a)}
.video .title{left:60px;top:12px;background:rgba(0,0,0,.78);padding:6px 10px;width:330px}
.video .title b{display:block;font-family:'Arimo',sans-serif;font-size:16px;color:#3fb6ff;line-height:19px}
.video .title span{font-size:11px;color:#ddd}
.video .badge{left:0;top:14px;width:52px;height:52px;background:#6b5a48}
.video .tools{right:10px;top:12px;display:flex;flex-direction:column;gap:6px}
.video .tools i{display:block;width:40px;height:38px;background:rgba(0,0,0,.8);color:#fff;font-style:normal;font-size:9px;text-align:center;padding-top:24px}
.video .bar{left:6px;bottom:6px;right:6px;height:34px;background:rgba(0,0,0,.85);display:flex;align-items:center;gap:10px;padding:0 8px}
.video .play{width:44px;height:26px;background:#333;display:flex;align-items:center;justify-content:center}
.video .track{flex:1;height:8px;background:#444}
.video .track i{display:block;width:30%;height:100%;background:#3fb6ff}
.plan{left:704px;top:1284px;width:338px;height:296px;border:3px solid #3a3a3a;background:#111}
.plan .pic{left:0;top:0;width:158px;height:290px;background:linear-gradient(180deg,#bfbfbf,#6b6b6b 40%,#a0703a 60%,#333)}
.plan .txt{left:172px;top:18px;font-family:'Oswald',sans-serif;color:var(--white)}
.plan .txt p{font-size:15px;margin-bottom:12px}
.plan .txt ul{list-style:none;padding-left:18px;font-size:15px;line-height:26px;color:var(--muted)}
.btn{position:absolute;background:var(--magenta);color:var(--white);font-family:'Oswald',sans-serif;font-size:15px;text-align:center;width:90px;height:24px;line-height:24px}
.feature{top:1657px;width:434px;height:312px;border:3px solid #3a3a3a;background:#0d0d0d}
.feature .pic{left:0;top:0;width:180px;height:306px}
.feature h4{position:absolute;left:190px;top:12px;font-family:'Freckle Face',cursive;font-weight:400;font-size:28px;color:var(--magenta);line-height:30px}
.feature p{position:absolute;left:190px;top:88px;width:228px;font-size:13px;line-height:19px;color:#cfcfcf}
.project{left:158px;width:532px;height:116px;display:flex;background:#1d1d1d}
.project .date{width:94px;background:var(--magenta);color:var(--white);font-family:'Oswald',sans-serif;text-align:center;padding-top:14px;font-size:40px;line-height:44px}
.project .date span{display:block;font-size:30px;line-height:38px}
.project .pic{width:207px;background:linear-gradient(90deg,#4a4a4a,#9a9a9a 50%,#3a3a3a)}
.project .pic.warm{background:linear-gradient(90deg,#b82d5a,#e6a04a 50%,#5a2a6a)}
.project .info{padding:20px 0 0 20px;font-family:'Oswald',sans-serif}
.project .info b{display:block;font-weight:400;font-size:17px;color:var(--white)}
.project .info .loc{font-family:'Arimo',sans-serif;font-size:12px;color:var(--muted);display:flex;align-items:center;gap:6px;margin-top:4px}
.project .info .gal{display:block;font-family:'Arimo',sans-serif;font-size:12px;color:var(--magenta);margin-top:22px}
.testimonial{left:704px;width:338px}
.testimonial .avatar{position:absolute;left:4px;top:0;width:96px;height:116px;background:linear-gradient(180deg,#d8d8d8,#8a8a8a)}
.testimonial .who{position:absolute;left:109px;top:12px;font-family:'Oswald',sans-serif;font-size:15px;color:var(--white)}
.testimonial .who small{display:block;font-size:12px;color:var(--muted)}
.testimonial p{position:absolute;left:4px;top:124px;width:330px;font-size:12.5px;line-height:18px;color:#cfcfcf}
.all{left:708px;top:2580px;font-size:12px;color:var(--magenta)}
.footer{left:0;top:2652px;width:1200px;height:144px;background:#0b0b0b;border-top:4px solid #2a2a2a}
.footer nav{position:absolute;left:0;width:1200px;top:30px;display:flex;justify-content:center;gap:22px;font-family:'Oswald',sans-serif;font-size:13px;color:var(--muted)}
.footer .legal{position:absolute;left:0;width:1200px;top:70px;text-align:center;font-size:11px;line-height:18px;color:#7a7a7a}
</style>
</head>
<body>
<div class="page"></div>

<header>
  <div class="abs logo">Bramblewick</div>
  <div class="abs logo-sub">ENTERTAINMENT · Vancouver, Calgary, Toronto</div>
  <div class="abs tagline">BRINGING YOUR IDEAS TO LIFE</div>
  <span class="abs social" style="left:912px"></span>
  <span class="abs social" style="left:959px"></span>
  <span class="abs social" style="left:1006px"></span>
  <div class="abs contact">
    <div class="phone">CONTACT US: 604-555-0147</div>
    <div class="email">email us: info@bramblewickentertainment.example</div>
  </div>
</header>

<nav class="abs nav">
  <span>CORPORATE EVENTS</span><span>PRIVATE PARTIES</span><span>COMMUNITY EVENTS</span><span>FILM &amp; TV</span><span>BUSINESS PROMOTIONS</span><span>CUSTOM ENTERTAINMENT</span>
</nav>

<div class="abs hero" role="img" aria-label="Concert crowd with raised hands under blue stage lights"></div>
<div class="abs hero-caption">YOUR BEST CONNECTION FOR<br>UNFORGETTABLE ENTERTAINMENT</div>
<div class="abs dots"><i></i><i></i><i></i><i></i><i></i></div>

<h2 class="heading" style="left:158px;top:640px;width:884px">Service</h2>

<section class="abs svc" style="left:158px;top:702px">
  <div class="txt"><h3>Bramblewick's Characters</h3>
    <ul><li>Star-studded impersonators</li><li>Roving Characters</li><li>Improv Artists</li><li>Comedians</li><li>Singing Telegrams</li><li>Professional Actors &amp; Models</li><li>Emcees</li></ul></div>
  <div class="pic" role="img" aria-label="Black and white photo of performers in costume"></div>
</section>
<section class="abs svc" style="left:610px;top:702px">
  <div class="txt"><h3>Enchantment &amp; Adornment</h3>
    <ul><li>Firespinners</li><li>Living Statues</li><li>Stiltwalkers</li><li>Aerial Artists</li><li>Face &amp; Body Art</li><li>Airbrush Tattoos</li><li>Henna</li></ul></div>
  <div class="pic" role="img" aria-label="Black and white photo of body art model"></div>
</section>
<section class="abs svc" style="left:158px;top:960px">
  <div class="txt"><h3>Dance to the Music</h3>
    <ul><li>DJs</li><li>Live Bands</li><li>Musicians</li><li>Singers</li><li>Musical Improv</li><li>Hip Hop Dancers</li><li>Bhangara Dancing</li><li>Belly Dancing</li></ul></div>
  <div class="pic" role="img" aria-label="Dance troupe performing on stage" style="background:linear-gradient(180deg,#2a3a6a,#7a5a9a 50%,#2a1a3a)"></div>
</section>
<section class="abs svc" style="left:610px;top:960px">
  <div class="txt"><h3>For the Young and Young at Heart</h3>
    <ul><li>Fantasy Face Painting</li><li>Balloon Twisting</li><li>Live Interactive Shows</li><li>Magicians</li><li>Jugglers</li><li>Caricaturists</li><li>Mascots</li></ul></div>
  <div class="pic" role="img" aria-label="Black and white photo of a juggler inside a painted ring"></div>
</section>

<h2 class="heading" style="left:158px;top:1225px;width:532px">Last Video</h2>
<h2 class="heading" style="left:704px;top:1225px;width:338px">Event Planning</h2>

<div class="abs video" role="img" aria-label="Video still from a shopping centre grand opening event">
  <div class="abs badge"></div>
  <div class="abs title"><b>Grand Opening Events for the Shops at Harbour Lane</b><span>from: Bramblewick Entertainment</span></div>
  <div class="abs tools"><i>LIKE</i><i>SHARE</i><i>EMBED</i></div>
  <div class="abs bar">
    <div class="play"><svg width="14" height="14" viewBox="0 0 14 14"><path d="M2 1l11 6-11 6z" fill="#fff"/></svg></div>
    <div class="track"><i></i></div>
    <svg width="40" height="14" viewBox="0 0 40 14"><rect x="0" y="2" width="26" height="10" fill="#3fb6ff"/><path d="M30 2h8v10h-8z" fill="none" stroke="#fff" stroke-width="1.5"/></svg>
  </div>
</div>

<div class="abs plan">
  <div class="abs pic" role="img" aria-label="Collage of event photos with costumed performers"></div>
  <div class="abs txt">
    <p>Customize your...</p>
    <ul><li>Wedding</li><li>Birthday</li><li>Stag/Stagette</li><li>Grad Party</li><li>Dinner Party</li><li>Holiday Party</li></ul>
  </div>
  <span class="btn" style="left:205px;top:233px">More</span>
</div>

<h2 class="heading" style="left:158px;top:1600px;width:434px">Book Your Winter Entertainment Today</h2>
<h2 class="heading" style="left:610px;top:1600px;width:432px">This Mont's Featured Art</h2>

<article class="abs feature" style="left:158px">
  <div class="abs pic" role="img" aria-label="Black and white photo of a glamorous screen-star impersonator" style="background:linear-gradient(180deg,#cfcfcf,#5a5a5a)"></div>
  <h4>How to Make Surprise</h4>
  <p>There's no better way to send your message, flowers or balloons than with a customized character at a location of your choosing.<br>Our brave singers/actors will create an unforgettable experience. Ask about our Starlet Rose and Crooner Jack singers!</p>
  <span class="btn" style="left:185px;top:268px">More</span>
</article>
<article class="abs feature" style="left:610px">
  <div class="abs pic" role="img" aria-label="Golden living statue performer at a banquet hall" style="background:linear-gradient(180deg,#5a5448,#b08a3a 50%,#3a3428)"></div>
  <h4>Living Statues</h4>
  <p>Our customized "Golden Statues of Dawn" have been welcoming literally hundreds of guests at reception halls throughout Surrey at venues such as Lakeview Banquet Hall, Grand Regal Palace and Cedarline Banquet Hall.</p>
  <span class="btn" style="left:185px;top:268px">More</span>
</article>

<h2 class="heading" style="left:158px;top:2018px;width:532px">Latest Projects</h2>
<h2 class="heading" style="left:704px;top:2018px;width:338px">What They Say</h2>

<div class="abs project" style="top:2072px"><div class="date">29<span>Sep</span></div><div class="pic warm" role="img" aria-label="Colour photo of birthday party guests"></div><div class="info"><b>Birthday Party</b><span class="loc"><svg width="10" height="14" viewBox="0 0 10 14"><path d="M5 0a5 5 0 0 0-5 5c0 4 5 9 5 9s5-5 5-9a5 5 0 0 0-5-5zm0 7a2 2 0 1 1 0-4 2 2 0 0 1 0 4z" fill="#888"/></svg>Chicago, Illinois</span><span class="gal">Gallery »</span></div></div>
<div class="abs project" style="top:2213px"><div class="date">29<span>Sep</span></div><div class="pic" role="img" aria-label="Black and white photo of birthday party guests"></div><div class="info"><b>Birthday Party</b><span class="loc"><svg width="10" height="14" viewBox="0 0 10 14"><path d="M5 0a5 5 0 0 0-5 5c0 4 5 9 5 9s5-5 5-9a5 5 0 0 0-5-5zm0 7a2 2 0 1 1 0-4 2 2 0 0 1 0 4z" fill="#888"/></svg>Chicago, Illinois</span><span class="gal">Gallery »</span></div></div>
<div class="abs project" style="top:2353px"><div class="date">29<span>Sep</span></div><div class="pic" role="img" aria-label="Black and white photo of birthday party guests"></div><div class="info"><b>Birthday Party</b><span class="loc"><svg width="10" height="14" viewBox="0 0 10 14"><path d="M5 0a5 5 0 0 0-5 5c0 4 5 9 5 9s5-5 5-9a5 5 0 0 0-5-5zm0 7a2 2 0 1 1 0-4 2 2 0 0 1 0 4z" fill="#888"/></svg>Chicago, Illinois</span><span class="gal">Gallery »</span></div></div>
<div class="abs project" style="top:2495px"><div class="date">29<span>Sep</span></div><div class="pic" role="img" aria-label="Black and white photo of birthday party guests"></div><div class="info"><b>Birthday Party</b><span class="loc"><svg width="10" height="14" viewBox="0 0 10 14"><path d="M5 0a5 5 0 0 0-5 5c0 4 5 9 5 9s5-5 5-9a5 5 0 0 0-5-5zm0 7a2 2 0 1 1 0-4 2 2 0 0 1 0 4z" fill="#888"/></svg>Chicago, Illinois</span><span class="gal">Gallery »</span></div></div>

<div class="abs testimonial" style="top:2072px">
  <div class="avatar" role="img" aria-label="Portrait photo of client"></div>
  <div class="who">Corinne T., New York<small>Anniversary Party</small></div>
  <p>Nam pretium turpis et arcu. Duis arcu tortor, suscipit eget, imperdiet nec, imperdiet iaculis, ipsum. Sed aliquam ultrices mauris. Integer ante arcu, accumsan a, consectetuer eget, posuere ut, mauris. Thank you Guys!</p>
</div>
<div class="abs testimonial" style="top:2333px">
  <div class="avatar" role="img" aria-label="Portrait photo of client"></div>
  <div class="who">Corinne T., New York<small>Anniversary Party</small></div>
  <p>Nam pretium turpis et arcu. Duis arcu tortor, suscipit eget, imperdiet nec, imperdiet iaculis, ipsum. Sed aliquam ultrices mauris. Integer ante arcu, accumsan a, consectetuer eget, posuere ut, mauris. Thank you Guys!</p>
</div>
<a class="abs all">All Testimonials »</a>

<footer class="abs footer">
  <nav><span>HOLIDAY PARTIES</span><span>WEDDINGS</span><span>BIRTHDAYS</span><span>STAG &amp; STAGETTES</span><span>ANNIVERSARIES</span><span>SPORTING EVENTS</span></nav>
  <div class="legal">Terms and Conditions | Privacy Policy<br>Copyright 2012. All Rights Reserved. BramblewickEntertainment.example</div>
</footer>
</body>
</html>
```